New Business Card Design Project

I have a logo I would like to use on the business card. I want something that will stand out and that will be remembered.

Target Market(s)

People who collect gems, minerals and crystals.

Contact Information for Business Card

email - mkthestonefalcon@vendrollo.com
phone # 917-406-2581

Font styles to use
Serif
Sans Serif
Decorative

Colors

Designer to choose colors to be used in the design.

Requirements
Must have
• The logo...two to choose from.
Nice to have
• An eye catching and memorable way to draw in people who collect gems minerals and crystals.

```html
<!DOCTYPE html>
<html lang="en">
<head>
<meta charset="utf-8">
<title>The Stone Falcon – Business Card</title>
<link rel="stylesheet" href="https://fonts.googleapis.com/css2?family=Lato:wght@400;700;900&display=swap">
<style>
  :root {
    --royal: #0505b8;
    --ink: #050505;
    --white: #ffffff;
    --stage: #d9d9d9;
    --soft: #c9c9e8;
  }
  * { box-sizing: border-box; margin: 0; padding: 0; }
  html, body { width: 1200px; height: 782px; overflow: hidden; }
  body {
    background: var(--stage);
    font-family: "Lato", Arial, sans-serif;
    position: relative;
  }
  .card {
    position: absolute;
    left: 310px;
    width: 580px;
    height: 331px;
    overflow: hidden;
    box-shadow: 0 6px 18px rgba(0,0,0,0.25);
  }
  .card--front { top: 40px; background: var(--royal); }
  .card--back { top: 411px; background: var(--ink); }

  .front__brand {
    position: absolute;
    left: 0; right: 0; top: 112px;
    text-align: center;
    color: var(--white);
    font-weight: 900;
    font-size: 40px;
    letter-spacing: 1px;
    text-transform: uppercase;
  }
  .front__web {
    position: absolute;
    left: 190px; width: 200px; top: 228px;
    text-align: center;
    color: var(--white);
    font-size: 15px;
    padding: 6px 0;
    border-top: 1px solid var(--white);
    border-bottom: 1px solid var(--white);
  }

  .back__brand {
    position: absolute;
    left: 0; right: 0; top: 62px;
    text-align: center;
  }
  .back__name {
    color: var(--white);
    font-weight: 900;
    font-size: 38px;
    text-transform: uppercase;
    letter-spacing: 1px;
    line-height: 1;
  }
  .back__tagline {
    margin-top: 8px;
    color: var(--soft);
    font-size: 10px;
    letter-spacing: 3px;
    text-transform: uppercase;
  }
  .back__person {
    position: absolute;
    left: 42px; top: 176px;
    font-size: 20px;
    display: flex;
    gap: 14px;
    align-items: baseline;
  }
  .person__name { color: var(--royal); text-transform: uppercase; font-weight: 400; letter-spacing: 0.5px; }
  .person__title { color: var(--white); font-size: 16px; }

  .back__band {
    position: absolute;
    left: 0; right: 0; bottom: 0;
    height: 110px;
    background: var(--royal);
    color: var(--white);
    padding: 20px 42px;
    font-size: 17px;
    line-height: 1.75;
  }
  .band__label { font-weight: 700; }
</style>
</head>
<body>
  <section class="card card--front">
    <div class="front__brand">The Stone Falcon</div>
    <div class="front__web">www.thestonefalcon.com</div>
  </section>

  <section class="card card--back">
    <div class="back__brand">
      <div class="back__name">The Stone Falcon</div>
      <div class="back__tagline">Gems · Minerals · Crystals</div>
    </div>
    <div class="back__person">
      <span class="person__name">Marcus Keller</span>
      <span class="person__title">Managing Director</span>
    </div>
    <div class="back__band">
      <div><span class="band__label">P:</span> 917-406-2581 | <span class="band__label">E:</span> mkthestonefalcon@vendrollo.com</div>
    </div>
  </section>
</body>
</html>
```